The Petalune Atelier Sticker Set

We are a flower shop who is creating a colorful DIY style box with cut flowers in a holograph bouquet paper. (Attached sample box)
Colors are yet to be finalized + the text inside too.
I am looking to include sticker sets with the flowers inside preferably as sticker sheets not individual stickers.
I need 3-5 Sticker Sheets and they can be icons, graphic images of flowers, quotes, words. I will include some of the ones I want as part of the set, feel free to suggest others.
Sticker Options:
1. Quotes
“ In an endless garden of flowers, I will always pick you”
“Petalune Club”
“Petalune at heart”
“You deserve flowers today and everyday”
“I got you flowers today”
“ You belong along the wildflowers”
“I must have flowers always & always”
Option for a sheet with horoscope flowers? Each sign and a flower type
Option for Alphabets
Option for heart/flower cute stickers / logo inspired
Stickers can be gifted as part of the box or used to decorate the box since it will be raw carton.
I also potentially want a card that can be used with this box (plain) in which they can stick these stickers on + write a message.
Sticker sheet can be 10 x 15 / 20 x 10

```html
<!DOCTYPE html>
<html lang="en">
<head>
<meta charset="utf-8">
<title>Petalune Atelier Sticker Set</title>
<link href="https://fonts.googleapis.com/css2?family=Montserrat:wght@400;600&family=Shrikhand&family=Chewy&family=Yellowtail&display=swap" rel="stylesheet">
<style>
  :root {
    --wine: #8c2f3f;
    --linen: #dbd8cc;
    --paper: #ffffff;
    --lily: #c9d6d3;
    --shadow: rgba(60, 40, 40, 0.25);
  }
  * { margin: 0; padding: 0; box-sizing: border-box; }
  html, body { width: 675px; height: 1200px; overflow: hidden; background: var(--paper); }
  body { position: relative; font-family: "Montserrat", sans-serif; color: #222; }

  .rule { position: absolute; background: var(--wine); }
  .rule--v { width: 1px; }
  .rule--h { height: 1px; }

  .quote-sticker { position: absolute; overflow: visible; filter: drop-shadow(2px 3px 2px var(--shadow)); }
  .quote-sticker text { text-anchor: middle; }
  .font-retro { font-family: "Shrikhand", serif; }
  .font-round { font-family: "Chewy", sans-serif; }
  .font-script { font-family: "Yellowtail", cursive; }

  .layer-edge { fill: var(--wine); stroke: var(--wine); stroke-linejoin: round; }
  .layer-pad  { fill: var(--linen); stroke: var(--linen); stroke-linejoin: round; }
  .layer-ink  { fill: var(--wine); }
  .layer-cream { fill: var(--linen); }

  .section-title {
    position: absolute; left: 0; width: 675px; text-align: center;
    font-size: 14px; font-weight: 400; color: #222;
  }

  .card {
    position: absolute; width: 196px; height: 132px;
    background: var(--linen);
    box-shadow: 3px 4px 5px var(--shadow);
  }
  .card--wine { background: var(--wine); }
  .card__frame { position: absolute; inset: 0; }
  .card__brand {
    position: absolute; left: 0; width: 100%; text-align: center;
    font-weight: 600; font-size: 8px; letter-spacing: 0.8px; line-height: 11px;
    color: var(--wine);
  }
  .card__brand--light { color: var(--linen); }
  .card__mark {
    position: absolute; left: 50%; width: 14px; height: 14px; margin-left: -7px;
    border: 1.2px solid var(--wine); border-radius: 50%;
  }
  .card__line { position: absolute; left: 9px; right: 10px; height: 1px; background: var(--wine); opacity: .7; }
  .card__thanks { position: absolute; inset: 0; overflow: visible; }
  .card__thanks text { text-anchor: middle; }

  .wrapping-paper {
    position: absolute; left: 29px; top: 789px; width: 393px; height: 361px;
    background: linear-gradient(135deg, var(--linen), #cfb9b4 50%, var(--linen));
    box-shadow: 3px 4px 6px var(--shadow);
  }

  .seal { position: absolute; left: 455px; width: 178px; height: 178px; }
  .seal text { font-family: "Montserrat", sans-serif; }
</style>
</head>
<body>

  <div class="rule rule--v" style="left:226px; top:56px; height:428px;"></div>
  <div class="rule rule--v" style="left:448px; top:47px; height:429px;"></div>
  <div class="rule rule--h" style="left:31px; top:261px; width:613px;"></div>

  <!-- Petalune Club -->
  <svg class="quote-sticker" style="left:20px; top:95px;" width="200" height="115" viewBox="0 0 200 115">
    <defs>
      <g id="club-words" class="font-retro" transform="rotate(-8 100 60)">
        <text x="100" y="52" font-size="34" textLength="170" lengthAdjust="spacingAndGlyphs">Petalune</text>
        <text x="112" y="97" font-size="44" textLength="110" lengthAdjust="spacingAndGlyphs">Club</text>
      </g>
    </defs>
    <use href="#club-words" class="layer-edge" stroke-width="16"/>
    <use href="#club-words" class="layer-pad" stroke-width="11"/>
    <use href="#club-words" class="layer-ink"/>
  </svg>

  <!-- You deserve flowers -->
  <svg class="quote-sticker" style="left:240px; top:68px;" width="195" height="142" viewBox="0 0 195 142">
    <defs>
      <g id="deserve-words" class="font-round" transform="rotate(-3 97 90)">
        <text x="90" y="66" font-size="28" textLength="140" lengthAdjust="spacingAndGlyphs">you deserve</text>
        <text x="95" y="96" font-size="28" textLength="170" lengthAdjust="spacingAndGlyphs">flowers today</text>
        <text x="92" y="126" font-size="28" textLength="140" lengthAdjust="spacingAndGlyphs">and everyday</text>
      </g>
    </defs>
    <circle cx="150" cy="30" r="22" fill="var(--lily)" stroke="var(--linen)" stroke-width="5" role="img" aria-label="Pale blue lily illustration"/>
    <use href="#deserve-words" class="layer-edge" stroke-width="20"/>
    <use href="#deserve-words" class="layer-pad" stroke-width="15"/>
    <use href="#deserve-words" class="layer-ink"/>
  </svg>

  <!-- Petalune at heart -->
  <svg class="quote-sticker" style="left:478px; top:108px;" width="160" height="95" viewBox="0 0 160 95">
    <defs>
      <g id="heart-words" class="font-retro" transform="rotate(-6 80 50)">
        <text x="82" y="44" font-size="32" textLength="140" lengthAdjust="spacingAndGlyphs">Petalune</text>
        <text x="78" y="82" font-size="32" textLength="125" lengthAdjust="spacingAndGlyphs">at heart</text>
      </g>
    </defs>
    <use href="#heart-words" class="layer-edge" stroke-width="8"/>
    <use href="#heart-words" class="layer-pad" stroke-width="4"/>
    <use href="#heart-words" class="layer-ink"/>
  </svg>

  <!-- I got you flowers today -->
  <svg class="quote-sticker" style="left:28px; top:330px;" width="170" height="105" viewBox="0 0 170 105">
    <defs>
      <text id="got-you" class="font-round" x="92" y="32" font-size="32" textLength="145" lengthAdjust="spacingAndGlyphs">i GOT YOU</text>
      <text id="got-flowers" class="font-script" x="86" y="76" font-size="54" textLength="150" lengthAdjust="spacingAndGlyphs">Flowers</text>
      <text id="got-today" class="font-round" x="128" y="100" font-size="20" textLength="62" lengthAdjust="spacingAndGlyphs">TODAY</text>
    </defs>
    <use href="#got-you" class="layer-pad" stroke-width="6"/>
    <use href="#got-you" class="layer-ink"/>
    <use href="#got-flowers" class="layer-pad" stroke-width="12"/>
    <use href="#got-flowers" class="layer-cream" stroke="var(--wine)" stroke-width="2"/>
    <use href="#got-today" class="layer-pad" stroke-width="6"/>
    <use href="#got-today" class="layer-ink"/>
  </svg>

  <!-- You belong along the wildflowers -->
  <svg class="quote-sticker" style="left:246px; top:328px;" width="165" height="100" viewBox="0 0 165 100">
    <path d="M16 3 L18 11 L26 13 L18 15 L16 23 L14 15 L6 13 L14 11 Z M26 18 L27 21 L30 22 L27 23 L26 26 L25 23 L22 22 L25 21 Z" fill="var(--wine)"/>
    <path d="M142 74 L144 82 L152 84 L144 86 L142 94 L140 86 L132 84 L140 82 Z M153 84 L154 87 L157 88 L154 89 L153 92 L152 89 L149 88 L152 87 Z" fill="var(--wine)"/>
    <g class="font-round layer-ink" transform="rotate(-3 82 50)">
      <text x="92" y="35" font-size="22" textLength="122" lengthAdjust="spacingAndGlyphs">YOU BELONG</text>
      <text x="90" y="56" font-size="22" textLength="110" lengthAdjust="spacingAndGlyphs">ALONG THE</text>
      <text x="80" y="78" font-size="22" textLength="148" lengthAdjust="spacingAndGlyphs">WILDFLOWERS</text>
    </g>
  </svg>

  <!-- I must have flowers -->
  <svg class="quote-sticker" style="left:464px; top:320px;" width="180" height="84" viewBox="0 0 180 84">
    <rect x="1" y="1" width="178" height="78" rx="14" fill="var(--linen)" stroke="var(--wine)" stroke-width="2"/>
    <rect x="6" y="6" width="168" height="26" rx="8" fill="var(--wine)"/>
    <text x="90" y="27" class="font-round layer-cream" font-size="21" textLength="150" lengthAdjust="spacingAndGlyphs">I MUST HAVE</text>
    <text x="90" y="63" class="font-round layer-ink" font-size="36" textLength="160" lengthAdjust="spacingAndGlyphs">FLOWERS</text>
    <rect x="40" y="64" width="100" height="14" rx="3" fill="var(--wine)"/>
    <text x="90" y="75" class="font-round layer-cream" font-size="10" textLength="84" lengthAdjust="spacingAndGlyphs">ALWAYS &amp; ALWAYS</text>
  </svg>

  <!-- thank you cards -->
  <div class="rule rule--h" style="left:31px; top:548px; width:238px;"></div>
  <div class="rule rule--h" style="left:405px; top:548px; width:239px;"></div>
  <h2 class="section-title" style="top:538px;">Thankyou Card</h2>

  <div class="card" style="left:31px; top:574px;">
    <svg class="card__frame" viewBox="0 0 196 132" aria-hidden="true">
      <path d="M13 5 H183 A8 8 0 0 0 191 13 V119 A8 8 0 0 0 183 127 H13 A8 8 0 0 0 5 119 V13 A8 8 0 0 0 13 5 Z" fill="none" stroke="var(--wine)" stroke-width=".8"/>
    </svg>
    <div class="card__mark" style="top:38px;"></div>
    <p class="card__brand" style="top:61px;">THE PETALUNE ATELIER<br>DUBAI</p>
  </div>

  <div class="card card--wine" style="left:239px; top:574px;">
    <p class="card__brand card__brand--light" style="top:14px; font-size:7px;">PETALUNE ATELIER</p>
    <svg class="card__thanks" viewBox="0 0 196 132">
      <defs>
        <g id="thanks-words" class="font-retro" transform="rotate(-6 98 80)">
          <text x="92" y="72" font-size="38" textLength="118" lengthAdjust="spacingAndGlyphs">Thank</text>
          <text x="122" y="108" font-size="38" textLength="80" lengthAdjust="spacingAndGlyphs">You</text>
        </g>
      </defs>
      <use href="#thanks-words" class="layer-pad" stroke-width="12"/>
      <use href="#thanks-words" class="layer-edge" stroke-width="8"/>
      <use href="#thanks-words" class="layer-cream"/>
    </svg>
  </div>

  <div class="card" style="left:448px; top:574px;">
    <svg class="card__frame" viewBox="0 0 196 132" aria-hidden="true">
      <path d="M13 5 H183 A8 8 0 0 0 191 13 V119 A8 8 0 0 0 183 127 H13 A8 8 0 0 0 5 119 V13 A8 8 0 0 0 13 5 Z" fill="none" stroke="var(--wine)" stroke-width=".8"/>
    </svg>
    <div class="card__mark" style="top:18px;"></div>
    <p class="card__brand" style="top:46px;">THE PETALUNE ATELIER<br>DUBAI</p>
    <div class="card__line" style="top:76px;"></div>
    <div class="card__line" style="top:88px;"></div>
    <div class="card__line" style="top:102px;"></div>
  </div>

  <!-- paper & stickers -->
  <div class="rule rule--h" style="left:31px; top:754px; width:238px;"></div>
  <div class="rule rule--h" style="left:405px; top:754px; width:239px;"></div>
  <h2 class="section-title" style="top:744px;">paper &amp; stickers</h2>

  <div class="wrapping-paper" role="img" aria-label="Wrapping paper with repeating wine-red floral pattern on linen"></div>

  <svg class="seal" style="top:779px;" viewBox="0 0 178 178" role="img" aria-label="Round sticker: The Petalune Atelier Dubai">
    <defs>
      <path id="seal-top" d="M26 89 A63 63 0 0 1 152 89"/>
      <path id="seal-bottom" d="M34 89 A55 55 0 0 0 144 89"/>
    </defs>
    <circle cx="91" cy="91" r="88" fill="var(--shadow)" opacity=".5"/>
    <circle cx="89" cy="89" r="88" fill="var(--wine)"/>
    <circle cx="89" cy="89" r="80" fill="none" stroke="var(--linen)" stroke-width="1"/>
    <text font-size="14" fill="var(--linen)" letter-spacing="1.5"><textPath href="#seal-top" startOffset="50%" text-anchor="middle">THE PETALUNE ATELIER</textPath></text>
    <text font-size="14" fill="var(--linen)" letter-spacing="2" dy="5"><textPath href="#seal-bottom" startOffset="50%" text-anchor="middle">DUBAI</textPath></text>
    <circle cx="89" cy="89" r="16" fill="none" stroke="var(--linen)" stroke-width="3"/>
  </svg>

  <svg class="seal" style="top:965px;" viewBox="0 0 178 178" role="img" aria-label="Round sticker: Petalune">
    <circle cx="91" cy="91" r="88" fill="var(--shadow)" opacity=".5"/>
    <circle cx="89" cy="89" r="88" fill="var(--linen)"/>
    <circle cx="89" cy="89" r="73" fill="none" stroke="var(--wine)" stroke-width="5"/>
    <text x="89" y="95" font-size="17" font-weight="600" fill="var(--wine)" text-anchor="middle" letter-spacing="1">PETALUNE</text>
  </svg>

</body>
</html>
```